Beacon Advisory Website

I currently have a website www.beaconadvisoryinc.example. We are a IT Consulting Company. Our website will pretty much tell out our services. I am looking to enhance my website and make it look more professional. Looking for very classy and Contemporary look and design for my website.

Industry/Entity Type

It Company

```html
<!DOCTYPE html>
<html lang="en">
<head>
<meta charset="utf-8">
<title>Beacon Advisory</title>
<link href="https://fonts.googleapis.com/css2?family=Arimo:wght@400;700&family=Open+Sans:wght@400;600&display=swap" rel="stylesheet">
<style>
  :root {
    --brand-blue: #2a7fbd;
    --navy: #1f3550;
    --hex-mid: #2c4a6e;
    --hex-dark: #2a3a4e;
    --accent-cream: #f6d99b;
    --submit-red: #d42426;
    --ink: #111111;
    --body-grey: #6b6b6b;
    --panel-grey: #f3f3f3;
    --band-grey: #f4f4f4;
    --white: #ffffff;
    --divider: #7a9cc8;
    --divider-dot: #8b5aa8;
  }
  * { margin: 0; padding: 0; box-sizing: border-box; }
  html, body { width: 738px; height: 1200px; overflow: hidden; background: var(--white); }
  body { position: relative; font-family: "Open Sans", Arial, sans-serif; color: var(--ink); }
  .abs { position: absolute; }

  /* Header */
  .site-header { position: absolute; left: 0; top: 0; width: 738px; height: 38px; background: var(--white); }
  .brand { position: absolute; left: 62px; top: 11px; display: flex; align-items: center; gap: 5px;
    font-family: "Arimo", Arial, sans-serif; font-weight: 700; font-size: 11px; color: var(--navy); letter-spacing: .3px; }
  .brand-mark { width: 14px; height: 14px; background: var(--brand-blue); border-radius: 50%; }
  .main-nav a { position: absolute; top: 13px; font-family: "Arimo", Arial, sans-serif; font-size: 7.5px; color: #333; text-decoration: none; }

  /* Hero */
  .hero { position: absolute; left: 0; top: 38px; width: 738px; height: 286px; background: var(--brand-blue); }
  .hero-title { position: absolute; left: 61px; top: 117px; font-family: "Arimo", Arial, sans-serif; font-size: 15.5px; font-weight: 400; color: var(--accent-cream); }
  .hero-copy { position: absolute; left: 61px; top: 148px; width: 370px; font-size: 7.3px; line-height: 13.5px; color: var(--white); }
  .btn-read { position: absolute; left: 61px; top: 250px; width: 72px; height: 23px; background: #0d0d0d; border-radius: 2px;
    color: var(--white); font-size: 6.3px; font-weight: 600; display: flex; align-items: center; justify-content: center; }
  .hero-portrait { position: absolute; left: 482px; top: 60px; width: 180px; height: 186px;
    background: linear-gradient(180deg, #3b86bf 0%, #2a7fbd 25%, #1c2636 60%, #11161f 100%); border-radius: 60px 60px 0 0; }

  /* Consultation form */
  .consult-card { position: absolute; left: 470px; top: 246px; width: 206px; height: 226px; background: var(--panel-grey); }
  .consult-title { position: absolute; left: 0; top: 20px; width: 206px; text-align: center; font-family: "Arimo", Arial, sans-serif;
    font-size: 13px; line-height: 17px; letter-spacing: .6px; color: var(--ink); }
  .field { position: absolute; left: 11px; width: 183px; height: 32px; background: var(--white); font-size: 8px; color: #555; padding: 11px 0 0 9px; }
  .field-name { top: 72px; }
  .field-email { top: 112px; }
  .btn-submit { position: absolute; left: 11px; top: 153px; width: 183px; height: 32px; background: var(--submit-red);
    color: var(--white); font-size: 8px; display: flex; align-items: center; justify-content: center; }
  .guarantee { position: absolute; left: 0; top: 199px; width: 206px; text-align: center; font-family: "Arimo", Arial, sans-serif; font-size: 8px; color: #555; }

  /* Services */
  .services-title { position: absolute; left: 61px; top: 347px; font-family: "Arimo", Arial, sans-serif; font-size: 13.5px; color: var(--ink); }
  .service-tile { position: absolute; width: 108px; height: 37px; background: var(--panel-grey); color: var(--brand-blue);
    font-family: "Arimo", Arial, sans-serif; font-size: 10.5px; display: flex; align-items: center; justify-content: center; }

  /* Section headings */
  .section-title { position: absolute; left: 0; width: 738px; text-align: center; font-family: "Arimo", Arial, sans-serif; font-size: 16px; color: var(--ink); }
  .section-divider { position: absolute; left: 336px; width: 66px; height: 8px; }
  .section-lede { position: absolute; left: 160px; width: 418px; text-align: center; font-size: 7.3px; line-height: 13.5px; color: var(--body-grey); }

  /* Features */
  .feature { position: absolute; width: 140px; text-align: center; }
  .feature-icon { display: block; margin: 0 auto; }
  .feature-title { margin-top: 18px; font-family: "Arimo", Arial, sans-serif; font-size: 10px; color: var(--ink); }
  .feature-copy { margin-top: 9px; font-size: 7.3px; line-height: 10.6px; color: var(--body-grey); padding: 0 10px; }

  /* Video */
  .video-band { position: absolute; left: 0; top: 794px; width: 738px; height: 406px; background: var(--band-grey); }
  .video-frame { position: absolute; left: 116px; top: 922px; width: 507px; height: 278px; background: #0b0b0b; padding-top: 4px; }
  .video-still { width: 100%; height: 100%; background: linear-gradient(120deg, #ece1c3 0%, #e6dbbd 45%, #e14f6a 62%, #4e8a86 78%, #1e3b40 100%); }
</style>
</head>
<body>

<header class="site-header">
  <div class="brand"><span class="brand-mark"></span>BEACON ADVISORY</div>
  <nav class="main-nav">
    <a style="left:334px">Company</a>
    <a style="left:393px">Service</a>
    <a style="left:445px">Solutions</a>
    <a style="left:502px">Resources</a>
    <a style="left:564px">Career</a>
    <a style="left:612px">Contact US</a>
  </nav>
</header>

<section class="hero">
  <div class="hero-portrait" role="img" aria-label="Photo of a smiling consultant in a dark suit and light blue tie"></div>
</section>
<h1 class="hero-title">Get the Best Solutionfor Your Business.</h1>
<p class="hero-copy">Today's IT market is a dynamic, fast-paced industry, with ever-increasing demands. Meeting these demands for over 25 years, Beacon Advisory maintains a global presence, aggressively recruiting expertly qualified IT and Management Professionals from around the world and cultivating key partnerships with corporations to understand their business models end-to-end, with a goal of delivering exceptional client service and ensuring a consistent delivery of the talent needed to drive results</p>
<div class="btn-read">Read More Here</div>

<aside class="consult-card">
  <h2 class="consult-title">GET A FREE<br>CONSULATION NOW !!</h2>
  <div class="field field-name">Name</div>
  <div class="field field-email">Email</div>
  <div class="btn-submit">Submit</div>
  <p class="guarantee">Satisfaction 100% Guranteed.</p>
</aside>

<h2 class="services-title">Servises In :</h2>
<div class="service-tile" style="left:62px;top:381px">Technology</div>
<div class="service-tile" style="left:185px;top:381px">Business</div>
<div class="service-tile" style="left:310px;top:381px">Application</div>
<div class="service-tile" style="left:62px;top:435px">Development</div>
<div class="service-tile" style="left:185px;top:435px">ENTP Integration</div>
<div class="service-tile" style="left:310px;top:435px">IT Consulting</div>

<h2 class="section-title" style="top:509px">What Makes Us The #1 Choice</h2>
<svg class="section-divider" style="top:533px" viewBox="0 0 66 8">
  <line x1="0" y1="4" x2="66" y2="4" stroke="var(--divider)" stroke-width="1"/>
  <rect x="30" y="1" width="6" height="6" transform="rotate(45 33 4)" fill="var(--white)" stroke="var(--divider-dot)" stroke-width="1.2"/>
</svg>
<p class="section-lede" style="top:549px">Lorem ipsum dolor sit amet, consectetur adipiscing elit. Vestibulum nibh neque, convallis ut interdum a, consequat sit amet mauris. Vivamus sed tincidunt enim.</p>

<div class="feature" style="left:94px;top:602px">
  <svg class="feature-icon" width="78" height="81" viewBox="0 0 78 81">
    <polygon points="39,0 78,20 78,61 39,81 0,61 0,20" fill="var(--brand-blue)"/>
    <rect x="21" y="27" width="36" height="26" fill="#f2c14e"/>
    <polyline points="21,27 39,42 57,27" fill="none" stroke="#d9a22c" stroke-width="2"/>
  </svg>
  <h3 class="feature-title">First Awesome Feature.</h3>
  <p class="feature-copy">Lorem ipsum dolor sit amet, Vestibulum nibh neque, convallis ut interdum a, consequat sit amet mauris.</p>
</div>
<div class="feature" style="left:299px;top:602px">
  <svg class="feature-icon" width="78" height="81" viewBox="0 0 78 81">
    <polygon points="39,0 78,20 78,61 39,81 0,61 0,20" fill="var(--hex-mid)"/>
    <polyline points="25,41 35,51 54,30" fill="none" stroke="#f3d2b3" stroke-width="6" stroke-linecap="round" stroke-linejoin="round"/>
  </svg>
  <h3 class="feature-title">Second Awesom Feature.</h3>
  <p class="feature-copy">Lorem ipsum dolor sit amet, Vestibulum nibh neque, convallis ut interdum a, consequat sit amet mauris.</p>
</div>
<div class="feature" style="left:504px;top:602px">
  <svg class="feature-icon" width="78" height="81" viewBox="0 0 78 81">
    <polygon points="39,0 78,20 78,61 39,81 0,61 0,20" fill="var(--hex-dark)"/>
    <path d="M27 25 H51 V33 Q51 45 39 47 Q27 45 27 33 Z" fill="#f2c12e"/>
    <rect x="36" y="47" width="6" height="7" fill="#f2c12e"/>
    <rect x="30" y="54" width="18" height="4" fill="#f2c12e"/>
  </svg>
  <h3 class="feature-title">Thrid Awesome Feature</h3>
  <p class="feature-copy">Lorem ipsum dolor sit amet, Vestibulum nibh neque, convallis ut interdum a, consequat sit amet mauris.</p>
</div>

<section class="video-band"></section>
<h2 class="section-title" style="top:827px">Watch Our Short Video Presentation</h2>
<svg class="section-divider" style="top:852px" viewBox="0 0 66 8">
  <line x1="0" y1="4" x2="66" y2="4" stroke="var(--divider)" stroke-width="1"/>
  <rect x="30" y="1" width="6" height="6" transform="rotate(45 33 4)" fill="var(--band-grey)" stroke="var(--divider-dot)" stroke-width="1.2"/>
</svg>
<p class="section-lede" style="top:868px">Lorem ipsum dolor sit amet, consectetur adipiscing elit. Vestibulum nibh neque, convallis ut interdum a, consequat sit amet mauris. Vivamus sed tincidunt enim.</p>
<div class="video-frame">
  <div class="video-still" role="img" aria-label="Video still: flat illustration of a man in a red sweater working at a computer, bicycle behind him"></div>
</div>

</body>
</html>
```